Steady Meadowcap HEMP Cannabis CBD tinctures

We need packaging for our line of CBD product label design based in Oakland Ca Brand is called 'Steady Meadowcap'. Our initial product is tincture to help people with pain with out the High effect of THC. I will be attaching og other company sample. The design should communicate slick look and relay health. Use the logo as way to color

Target Market(s)

CBD

Font styles to use
Serif
Decorative

Requirements
Must have
• Design that will make it stand out from the rest of the product on the shelve and be bright.
Nice to have
• The package must be able to stand out and not be dominated by Black color the green color must be the main color.
Should not have
• Be all black and get lost on the shelves

```html
<!DOCTYPE html>
<html lang="en">
<head>
<meta charset="utf-8">
<title>Steady Meadowcap CBD Tincture Label</title>
<link href="https://fonts.googleapis.com/css2?family=Roboto:wght@400;500;700&family=Roboto+Condensed:wght@400;700&family=Oswald:wght@600&display=swap" rel="stylesheet">
<style>
  :root {
    --bg: #fdfcd2;
    --green: #4cc456;
    --green-deep: #2f9e3b;
    --green-mid: #5fd068;
    --green-pale: #b8efbb;
    --label-white: #f3f7f3;
    --grey-rule: #c9cfc9;
    --ink: #2b2b2b;
    --ink-soft: #555;
    --badge-blue: #3a4fa8;
    --badge-red: #d23a3a;
  }
  * { box-sizing: border-box; margin: 0; padding: 0; }
  html, body { width: 1200px; height: 1200px; overflow: hidden; }
  body {
    background: var(--bg);
    font-family: "Roboto", Arial, sans-serif;
    color: var(--ink);
    position: relative;
  }
  .label {
    position: absolute;
    top: 320px;
    width: 540px;
    height: 560px;
    overflow: hidden;
    background: var(--label-white);
    box-shadow: 0 6px 24px rgba(0,0,0,0.08);
  }
  .label--front { left: 40px; }
  .label--back { left: 620px; }

  .label__pattern {
    position: absolute; inset: 0;
    background: linear-gradient(180deg, #f6faf6 0%, #eef5ee 100%);
  }
  .label__top-band {
    position: absolute; left: 0; right: 0; top: 0; height: 14px;
    background: var(--green-mid);
    border-bottom: 5px solid var(--grey-rule);
  }
  .label__bottom-band {
    position: absolute; left: 0; right: 0; bottom: 0; height: 64px;
    background: var(--green-pale);
  }

  /* Front */
  .front__tab {
    position: absolute; top: 14px; left: 50%; transform: translateX(-50%);
    background: var(--green-mid); color: #fff;
    font-size: 21px; font-weight: 400; letter-spacing: 0.5px; line-height: 1.2;
    padding: 3px 18px 5px; border-radius: 0 0 8px 8px;
  }
  .brand {
    position: absolute; left: 0; right: 0;
    display: flex; flex-direction: column; align-items: center;
    color: var(--green);
    font-weight: 700;
    line-height: 1.1;
  }
  .brand__square { background: var(--green); border-radius: 6px; }
  .front__brand { top: 72px; gap: 18px; font-size: 30px; }
  .front__brand .brand__square { width: 100px; height: 100px; }

  .front__strength {
    position: absolute; top: 252px; left: 50%; transform: translateX(-50%);
    width: 206px; height: 36px; background: var(--green);
    color: #fff; font-size: 28px; font-weight: 700;
    display: flex; align-items: center; justify-content: center;
  }
  .front__type {
    position: absolute; top: 298px; left: 50%; transform: translateX(-50%);
    width: 208px; padding: 3px 0; line-height: 1.2;
    border-top: 2px solid var(--grey-rule); border-bottom: 2px solid var(--grey-rule);
    text-align: center; color: var(--green);
    font-size: 22px; letter-spacing: 1px;
  }
  .front__cbd {
    position: absolute; top: 346px; left: 0; right: 0; text-align: center;
    font-family: "Oswald", "Roboto Condensed", sans-serif;
    font-weight: 600; font-size: 62px; line-height: 1; color: var(--green);
  }
  .front__base { position: absolute; left: 0; bottom: 0; }

  /* Back */
  .back__brand { top: 26px; gap: 8px; font-size: 14px; }
  .back__brand .brand__square { width: 40px; height: 40px; border-radius: 4px; }
  .back__use-title {
    position: absolute; top: 114px; left: 57px; width: 423px; height: 26px;
    background: var(--green); color: #fff;
    font-size: 18px; font-weight: 500; text-align: center; line-height: 26px;
  }
  .back__use-list {
    position: absolute; top: 146px; left: 75px; width: 390px;
    list-style: none; font-size: 16px; color: var(--ink-soft); line-height: 1.3;
  }
  .back__use-list li { padding-left: 14px; text-indent: -14px; }
  .back__use-list li::before { content: "• "; }
  .back__rule {
    position: absolute; top: 218px; left: 57px; width: 423px; height: 3px;
    background: var(--green);
  }
  .facts {
    position: absolute; top: 238px; left: 83px; width: 276px;
    border: 2px solid var(--ink); background: #fff;
    font-family: "Roboto Condensed", "Arial Narrow", sans-serif;
    font-size: 11px; color: var(--ink);
  }
  .facts__title { font-weight: 700; font-size: 21px; padding: 0 6px; line-height: 1.15; }
  .facts__meta { padding: 0 6px; line-height: 1.35; }
  .facts__meta--last { border-bottom: 4px solid var(--ink); padding-bottom: 2px; }
  .facts__row {
    display: flex; justify-content: space-between; padding: 1px 6px;
  }
  .facts__row--head { border-bottom: 2px solid var(--ink); }
  .facts__row--item { line-height: 1.2; align-items: baseline; }
  .facts__row--item span:last-child { font-size: 14px; }
  .facts__items { border-bottom: 2px solid var(--ink); padding: 2px 0; }
  .facts__note { padding: 2px 6px; line-height: 1.35; }

  .back__flag {
    position: absolute; top: 460px; left: 50%; transform: translateX(-50%);
    width: 54px; height: 38px;
    background: linear-gradient(180deg, #d84a4a 0%, #f3f3f3 50%, #3e53a8 100%);
  }
  .back__badge {
    position: absolute; top: 502px; left: 50%; transform: translateX(-50%);
    display: flex; font-size: 14px; font-weight: 700; line-height: 18px; color: #fff; white-space: nowrap;
    z-index: 2;
  }
  .back__badge span { padding: 0 6px; }
  .back__badge-blue { background: var(--badge-blue); }
  .back__badge-red { background: var(--badge-red); }
  .label--back .label__bottom-band { height: 48px; }
</style>
</head>
<body>
  <section class="label label--front">
    <div class="label__pattern" role="img" aria-label="Faint green hexagon cube pattern background"></div>
    <div class="label__top-band"></div>
    <div class="front__tab">TINCTURE</div>
    <div class="brand front__brand">
      <div class="brand__square"></div>
      <div class="brand__name">Steady Meadowcap</div>
    </div>
    <div class="front__strength">1500MG</div>
    <div class="front__type">HEMP EXTRACT</div>
    <div class="front__cbd">CBD</div>
    <div class="label__bottom-band"></div>
    <svg class="front__base" width="540" height="108" viewBox="0 0 540 108">
      <polygon points="132,20 276,0 420,20 420,108 132,108" fill="var(--green-deep)"/>
      <rect x="460" y="44" width="80" height="64" fill="var(--green-mid)" opacity="0.5"/>
    </svg>
  </section>

  <section class="label label--back">
    <div class="label__pattern" role="img" aria-label="Faint green hexagon cube pattern background"></div>
    <div class="label__top-band"></div>
    <div class="brand back__brand">
      <div class="brand__square"></div>
      <div class="brand__name">Steady Meadowcap</div>
    </div>
    <div class="back__use-title">SUGGESTED USE:</div>
    <ul class="back__use-list">
      <li>Shake well before using. Store in a cool, dry place, away from light.</li>
      <li>Do not use if seal is broken</li>
    </ul>
    <div class="back__rule"></div>
    <div class="facts">
      <div class="facts__title">Supplement Facts</div>
      <div class="facts__meta">Servings Size: 1/2 dropper (approx. 0.5 mL)</div>
      <div class="facts__meta facts__meta--last">Servings Per Bottle: Approx. 60</div>
      <div class="facts__row facts__row--head"><span>Amount/ Serving</span><span>Daily Value</span></div>
      <div class="facts__items">
        <div class="facts__row facts__row--item"><span>Hemp Oil (Seed &amp;Stalks)</span><span>38.7 mg</span></div>
        <div class="facts__row facts__row--item"><span>Hemp Extract</span><span>10 mg</span></div>
      </div>
      <div class="facts__note">Daily Value not established **<br>Hemp Extract is a natural constituent of hemp</div>
    </div>
    <div class="back__flag" role="img" aria-label="Small United States flag"></div>
    <div class="label__bottom-band"></div>
    <div class="back__badge">
      <span class="back__badge-blue">PROUDLY</span><span class="back__badge-red">MADE IN USA</span>
    </div>
  </section>
</body>
</html>
```